Business Card design for construction company

I would like a business card design for a construction company - Harlow Constructions. I have attached the ai logo file for use. I would like the card to be very smart and clean and incorporate only white and the two colours in the logo. I would like the card to have two sides. One side can just have the logo, the other with the relevant information.

Target Market(s)

Building and Construction Clients

Industry/Entity Type

Business

Contact Information for Business Card

Name: Tom Pardoe
Company: Harlow Constructions Pty Limited
Address: 14 Mallee Crescent Carrow Vale 2093
Phone: 0427 531 068
Email: tomp@harlowbuild-example.com.au

Font styles to use
Serif
Sans Serif

Requirements
Must have
• Details noted above
• Logo as provided
• Colours as in logo
• Square edges
• A font that compliments the logo
Should not have
• Any colour other than white and those in logo
• Rounded edges

```html
<!DOCTYPE html>
<html lang="en">
<head>
<meta charset="utf-8">
<title>Harlow Constructions – Business Card</title>
<link rel="stylesheet" href="https://fonts.googleapis.com/css2?family=Jost:wght@400&display=swap">
<style>
  :root {
    --page: #ffffff;
    --backdrop: #fdd9bb;
    --card: #ffffff;
    --charcoal: #5b5b5d;
    --sky: #00aeef;
    --ink: #4a4a4c;
  }
  * { margin: 0; padding: 0; box-sizing: border-box; }
  html, body { width: 1200px; height: 1200px; overflow: hidden; background: var(--page); }
  body { position: relative; font-family: "Jost", sans-serif; color: var(--ink); }

  .backdrop { position: absolute; left: 0; top: 174px; width: 1200px; height: 848px; background: var(--backdrop); }

  .card { position: absolute; top: 420px; width: 554px; height: 358px; background: var(--card); overflow: hidden; }
  .card--front { left: 35px; }
  .card--back { left: 614px; }

  .wordmark {
    position: absolute; left: 0; width: 100%; text-align: center;
    font-size: 27px; font-weight: 400; letter-spacing: 4px; text-transform: uppercase;
    color: var(--charcoal); white-space: nowrap;
  }
  .card--front .wordmark { top: 52px; }
  .card--back .wordmark { top: 161px; }

  .holder { position: absolute; left: 190px; top: 154px; font-size: 23px; color: var(--sky); }

  .contacts { position: absolute; left: 155px; top: 206px; list-style: none; }
  .contacts li { display: flex; align-items: center; height: 30px; font-size: 18px; color: var(--ink); }
  .contacts svg { width: 24px; height: 22px; margin-right: 10px; flex: none; }

  .footer-bar { position: absolute; bottom: 0; height: 27px; }
  .footer-bar--charcoal { left: 0; width: 306px; background: var(--charcoal); }
  .footer-bar--sky { left: 311px; width: 243px; background: var(--sky); }

  .band { position: absolute; left: 0; width: 100%; background: var(--charcoal); }
  .band--top { top: 0; height: 106px; }
  .band--bottom { bottom: 0; height: 107px; }
  .rule { position: absolute; height: 3px; background: var(--sky); }
  .rule--top { left: 276px; width: 278px; top: 109px; }
  .rule--bottom { left: 0; width: 276px; top: 245px; }
</style>
</head>
<body>
  <div class="backdrop"></div>

  <section class="card card--front">
    <div class="wordmark">Harlow Constructions</div>
    <div class="holder">Tom Pardoe</div>
    <ul class="contacts">
      <li>
        <svg viewBox="0 0 24 22" aria-hidden="true"><rect x="1" y="4" width="22" height="14" fill="#00aeef"/><path d="M1 4 L12 12 L23 4 M1 18 L9 10 M23 18 L15 10" stroke="#fff" stroke-width="1.6" fill="none"/></svg>
        14 Mallee Crescent Carrow Vale 2093
      </li>
      <li>
        <svg viewBox="0 0 24 22" aria-hidden="true"><path d="M6 2 C3 3 2 6 4 10 C7 16 11 19 16 20 C19 21 21 19 21 17 L17 14 L14 16 C11 14 9 12 8 9 L10 6 Z" fill="#00aeef"/></svg>
        0427 531 068
      </li>
      <li>
        <svg viewBox="0 0 24 22" aria-hidden="true"><circle cx="12" cy="11" r="10" fill="#00aeef"/><text x="12" y="15.5" text-anchor="middle" font-family="Jost, sans-serif" font-size="13" fill="#fff">@</text></svg>
        tomp@harlowbuild-example.com.au
      </li>
    </ul>
    <div class="footer-bar footer-bar--charcoal"></div>
    <div class="footer-bar footer-bar--sky"></div>
  </section>

  <section class="card card--back">
    <div class="band band--top"></div>
    <div class="rule rule--top"></div>
    <div class="wordmark">Harlow Constructions</div>
    <div class="rule rule--bottom"></div>
    <div class="band band--bottom"></div>
  </section>
</body>
</html>
```